Web Design for Employee Benefits / Corporate Insurance Solutions Firm - Using Divi (by Corvane Pix...

*Please use Divi from corvane pixels to create the design.

Company Name: Harbourline By Tomas(Logo attached)

Colour scheme: White / Teal / Aquamarine / Grey

We are a firm that provides the following solutions for businesses:
- employee medical benefits
- office insurance
- talent retention / long-service retirement solutions
- keyman insurance

We need a website to provide information about our services, as well as password portals for employees of each company that we take care of.

Portals would provide specific information for employees of each company:
- employee handbook
- plan benefits & references
- claim forms

The site would also list articles for Human Resource Professionals and give them information about latest updates in the employee benefits / corporate culture best practices.

Human Resource Executives, Managing Directors, Chief Finance Officers, Employees

Business Consultant

• Should be able to adjust the website widths & font sizes to be viewed on:
• - computer;
• - slatu;
• - smartphone

```html
<!DOCTYPE html>
<html lang="en">
<head>
<meta charset="utf-8">
<title>Harbourline By Tomas</title>
<link rel="stylesheet" href="https://fonts.googleapis.com/css2?family=EB+Garamond:wght@400;500;600&family=Open+Sans:wght@400&display=swap">
<style>
:root{
  --teal:#237b80;
  --teal-dark:#1e5f63;
  --aqua:#3fe8d6;
  --menu:#5f8f8b;
  --ink:#2b6f72;
  --body:#4f7f7f;
  --line:#8fe3d8;
  --white:#ffffff;
  --grey:#8a9a9a;
}
*{box-sizing:border-box;margin:0;padding:0}
html,body{width:970px;height:1200px;overflow:hidden;background:var(--white)}
body{position:relative;font-family:"EB Garamond",Georgia,serif;color:var(--ink)}
.abs{position:absolute}
.hero{left:4px;top:4px;width:953px;height:382px;background:linear-gradient(120deg,#cfd7c9 0%,#b8b79c 30%,#9c8a66 55%,#7f8a5a 75%,#c9d3bf 100%);overflow:hidden}
.hero::after{content:"";position:absolute;inset:0;background:rgba(255,255,255,.42)}
.navbar{left:160px;top:4px;width:797px;height:46px;background:var(--teal)}
.brand{left:4px;top:4px;width:216px;height:77px;background:var(--white);clip-path:polygon(0 0,72% 0,100% 100%,0 100%);display:flex;flex-direction:column;align-items:flex-start;justify-content:center;padding-left:22px;gap:4px}
.brand-mark{width:30px;height:30px;border-radius:50%;background:var(--aqua);margin-left:46px}
.brand-name{font-size:12px;letter-spacing:2.5px;color:var(--teal-dark)}
.nav-link{top:17px;font-size:14.5px;color:var(--white);letter-spacing:.5px}
.nav-active{left:540px;top:12px;width:108px;height:38px;background:var(--menu)}
.dropdown{left:540px;top:50px;width:222px;height:184px;background:var(--menu);box-shadow:0 2px 6px rgba(0,0,0,.25)}
.dropdown a{position:absolute;left:15px;color:var(--white);font-size:18px;text-decoration:none}
.dropdown hr{position:absolute;left:2px;width:205px;border:0;border-top:1.5px solid #e9f1f0}
.soc{top:22px;width:12px;height:12px;border-radius:50%;background:var(--white)}
.hero-title{left:30px;top:106px;font-size:38px;font-weight:600;color:#163f41;letter-spacing:.5px}
.hero-sub{left:30px;top:172px;width:480px;font-size:17.5px;line-height:29px;color:#1f3f40}
.email{left:29px;top:243px;width:201px;height:31px;border:1px solid #6d7a76;font-size:17px;color:var(--aqua);padding:3px 14px}
.subscribe{left:249px;top:243px;width:114px;height:31px;background:var(--aqua);color:var(--white);font-size:14px;text-align:center;line-height:31px;letter-spacing:.5px}
.dot{top:373px;width:7px;height:7px;border-radius:50%;background:var(--teal)}
.section-title{top:432px;font-size:20px;letter-spacing:1px;color:var(--ink)}
.section-title span{color:var(--aqua)}
.profile-text{left:30px;top:475px;width:480px;font-size:15.5px;line-height:20px;color:var(--body)}
.devices{left:38px;top:555px;width:372px;height:193px;background:linear-gradient(160deg,#3c4a4a,#7fa79a 45%,#2f3a3a);border-radius:6px}
.vline{left:560px;top:438px;width:1px;height:334px;background:var(--line)}
.hline{left:11px;top:772px;width:943px;height:1px;background:var(--line)}
.mini{display:flex;gap:5px}
.mini i{width:7px;height:7px;border-radius:50%;background:var(--teal)}
.learn{font-size:8.5px;text-decoration:underline;color:var(--ink);letter-spacing:.3px}
.icon-box{width:85px;height:82px;border:1.5px solid var(--line);background:var(--white);box-shadow:2px 3px 5px rgba(0,0,0,.18)}
.icon-box.filled{background:var(--aqua);border-color:var(--aqua)}
.sol-title{font-size:15px;font-weight:500;color:var(--ink)}
.sol-body{width:200px;font-size:13px;line-height:17px;color:var(--body)}
.partner{top:836px;font-family:"EB Garamond",Georgia,serif;font-size:15px;color:var(--teal);display:flex;align-items:center;gap:6px}
.partner i{width:14px;height:14px;background:var(--aqua)}
.footer{left:6px;top:942px;width:951px;height:248px;background:var(--teal);color:var(--white)}
.foot-col{position:absolute;top:30px}
.foot-col h3{font-weight:400;font-size:19px;letter-spacing:.5px;margin-bottom:13px}
.foot-col p{font-size:14px;line-height:14px;margin-bottom:10px}
.contact{font-family:"Open Sans",Arial,sans-serif;font-size:12.5px}
.foot-brand{left:790px;top:124px;display:flex;flex-direction:column;align-items:center;gap:6px}
.foot-brand i{width:30px;height:30px;border-radius:50%;background:var(--aqua)}
.foot-brand span{font-size:12px;letter-spacing:2.5px;color:var(--teal-dark)}
</style>
</head>
<body>

<div class="abs hero" role="img" aria-label="Soft-focus photo of a business meeting at a wooden desk with a phone and notes"></div>
<div class="abs navbar"></div>
<div class="abs brand"><i class="brand-mark"></i><span class="brand-name">HARBOURLINE BY TOMAS</span></div>

<svg class="abs" style="left:193px;top:19px" width="18" height="18" viewBox="0 0 18 18" aria-label="Search"><circle cx="7.5" cy="7.5" r="6" fill="none" stroke="#fff" stroke-width="1.6"/><line x1="12" y1="12" x2="17" y2="17" stroke="#fff" stroke-width="1.6"/></svg>

<div class="abs nav-active"></div>
<span class="abs nav-link" style="left:366px">HOME</span>
<span class="abs nav-link" style="left:441px">ABOUT US</span>
<span class="abs nav-link" style="left:555px">SOLUTION</span>
<span class="abs nav-link" style="left:660px">CONTACT US</span>

<i class="abs soc" style="left:798px"></i>
<svg class="abs" style="left:826px;top:22px" width="17" height="12" viewBox="0 0 17 12" aria-label="Email"><rect x=".7" y=".7" width="15.6" height="10.6" fill="none" stroke="#fff" stroke-width="1.3"/><path d="M1 1l7.5 6L16 1" fill="none" stroke="#fff" stroke-width="1.3"/></svg>
<i class="abs soc" style="left:859px"></i>
<i class="abs soc" style="left:881px"></i>
<svg class="abs" style="left:918px;top:17px" width="18" height="18" viewBox="0 0 18 18" aria-label="Account"><circle cx="9" cy="5" r="4.2" fill="#fff"/><path d="M1 18c0-5 3.5-7.5 8-7.5s8 2.5 8 7.5z" fill="#fff"/></svg>

<nav class="abs dropdown">
  <a style="top:16px">Medical benefits</a><hr style="top:44px">
  <a style="top:65px">Office insurance</a><hr style="top:93px">
  <a style="top:114px">Retirement solutions</a><hr style="top:142px">
  <a style="top:158px">Keyman insurance</a>
</nav>

<h1 class="abs hero-title">HARBOURLINE BY TOMAS</h1>
<p class="abs hero-sub">Human Resource Executives, Managing Directors, Chief Finance Officers, Employees. Human Resource Executives.</p>
<div class="abs email">Email Address</div>
<div class="abs subscribe">SUBSCRIBE</div>
<i class="abs dot" style="left:463px;background:#fff"></i>
<i class="abs dot" style="left:476px"></i>
<i class="abs dot" style="left:489px"></i>

<h2 class="abs section-title" style="left:30px">COMPANY <span>PROFILE</span></h2>
<p class="abs profile-text">Human Resource Executives, Managing Directors, Chief Finance Officers, Employees. Human Resource Executives, Managing Directors, Chief Finance Officers, Employees.</p>
<div class="abs devices" role="img" aria-label="The website shown on a desktop monitor, laptop, tablet and phone"></div>
<div class="abs mini" style="left:31px;top:749px"><i></i><i></i><i></i><i></i></div>
<span class="abs learn" style="left:469px;top:746px">LEARN MORE</span>

<div class="abs vline"></div>

<h2 class="abs section-title" style="left:624px">OUR <span>SOLUTION</span></h2>

<div class="abs icon-box filled" style="left:624px;top:478px">
  <svg width="85" height="82" viewBox="0 0 85 82" aria-label="Medical kit"><path d="M34 22v-6h17v6" fill="none" stroke="#fff" stroke-width="3"/><rect x="16" y="22" width="53" height="42" fill="none" stroke="#fff" stroke-width="3"/><path d="M42.5 32v22M31.5 43h22" stroke="#fff" stroke-width="5"/></svg>
</div>
<span class="abs sol-title" style="left:728px;top:473px">Employee Medical benefits</span>
<p class="abs sol-body" style="left:730px;top:497px">Many employees in the public and private sector depend on medical benefits to support their health and well-being, as well as that of their family members.</p>
<div class="abs mini" style="left:730px;top:590px"><i></i><i></i><i></i><i></i></div>
<span class="abs learn" style="left:874px;top:588px">LEARN MORE</span>

<div class="abs icon-box" style="left:624px;top:643px">
  <svg width="85" height="82" viewBox="0 0 85 82" aria-label="Briefcase"><path d="M35 28v-7h15v7" fill="none" stroke="#3fe8d6" stroke-width="2.5"/><rect x="13" y="28" width="59" height="38" fill="none" stroke="#3fe8d6" stroke-width="2.5"/><path d="M13 44h59" stroke="#3fe8d6" stroke-width="2.5"/><rect x="38" y="39" width="9" height="9" fill="#3fe8d6"/></svg>
</div>
<span class="abs sol-title" style="left:728px;top:638px">Office insurance</span>
<p class="abs sol-body" style="left:730px;top:659px">Many employees in the public and private sector depend on medical benefits to support their health and well-being, as well as that of their family members.</p>
<div class="abs mini" style="left:730px;top:749px"><i></i><i></i><i></i><i></i></div>
<span class="abs learn" style="left:874px;top:746px">LEARN MORE</span>

<div class="abs hline"></div>

<svg class="abs" style="left:10px;top:850px" width="10" height="16" viewBox="0 0 10 16" aria-label="Previous"><path d="M9 1L2 8l7 7" fill="none" stroke="#3fe8d6" stroke-width="1.5"/></svg>
<div class="abs partner" style="left:88px"><i></i>Pulseway Care</div>
<div class="abs partner" style="left:258px"><i></i>Cardia Plus</div>
<div class="abs partner" style="left:400px"><i></i>Lumen Eye Centre</div>
<div class="abs partner" style="left:570px"><i></i>Brightsmile Dental</div>
<div class="abs partner" style="left:770px"><i></i>Medivane</div>
<svg class="abs" style="left:943px;top:850px" width="10" height="16" viewBox="0 0 10 16" aria-label="Next"><path d="M1 1l7 7-7 7" fill="none" stroke="#3fe8d6" stroke-width="1.5"/></svg>

<footer class="abs footer">
  <div class="foot-col" style="left:53px">
    <h3>OUR COMPANY</h3>
    <p>Home</p><p>About us</p><p style="margin-top:14px">Solution</p><p style="margin-top:14px">Contact us</p>
  </div>
  <div class="foot-col" style="left:255px;top:24px">
    <h3>SERVICES</h3>
    <p>Review</p><p style="margin-top:14px">Consultation</p><p style="margin-top:14px;line-height:13px">Draft new<br>solution</p><p style="margin-top:14px">Eeview &amp; Assess</p><p style="margin-top:14px">Speaking engagement</p>
  </div>
  <div class="foot-col" style="left:463px">
    <h3>FORMS</h3>
    <p style="line-height:13px">Employee<br>hanbook</p><p style="line-height:13px">Plan benefits<br>&amp; references</p><p style="margin-top:12px">Claim forms</p>
  </div>
  <div class="foot-col" style="left:605px">
    <h3>CONTACT US</h3>
    <p style="line-height:17px">Harbourline By Tomas<br>(Europe)</p>
    <p class="contact" style="display:flex;align-items:center;gap:6px"><svg width="14" height="10" viewBox="0 0 14 10"><rect x=".6" y=".6" width="12.8" height="8.8" fill="none" stroke="#fff"/><path d="M1 1l6 5 6-5" fill="none" stroke="#fff"/></svg>info@harbourlinebytomas.com</p>
    <p class="contact" style="display:flex;align-items:center;gap:6px;margin-top:14px"><svg width="9" height="14" viewBox="0 0 9 14"><rect x=".6" y=".6" width="7.8" height="12.8" rx="1" fill="none" stroke="#fff"/></svg>+456 310 227</p>
  </div>
  <div class="foot-col" style="left:788px">
    <h3>FOLLOW US</h3>
    <div style="display:flex;gap:9px;align-items:center">
      <i style="width:12px;height:12px;border-radius:50%;background:#fff"></i>
      <svg width="16" height="11" viewBox="0 0 16 11" aria-label="Email"><rect x=".6" y=".6" width="14.8" height="9.8" fill="none" stroke="#fff" stroke-width="1.2"/><path d="M1 1l7 5.5L15 1" fill="none" stroke="#fff" stroke-width="1.2"/></svg>
      <i style="width:12px;height:12px;border-radius:50%;background:#fff"></i>
      <i style="width:12px;height:12px;border-radius:50%;background:#fff"></i>
    </div>
  </div>
  <div class="abs foot-brand"><i></i><span>HARBOURLINE</span></div>
</footer>

</body>
</html>
```